Marwick Ostrand Law website for a law firm

modern clean website for a small boutique law firm. Based in Sacramento, CA and the Bay Area. Practice areas of Family Law, Civil litigation, and Criminal Defense. We already have a logo design as well as attorney pictures to include on page.
Would like images of California included on site.
Would like site to go with Logo that is already designed...blue/grey/white colors.

Industry/Entity Type

Law Firm

Number of Pages Required

5+ page

Requirements
Must have
• I already have several pages of content drafted. Just need the pages with images to input content. Must be clean and modern feel. Want it to reflect California and small boutique feel that is provided personalized legal attention.
• Must have a page where I can blog or post articles on.

```html
<!DOCTYPE html>
<html lang="en">
<head>
<meta charset="utf-8">
<title>Marwick Ostrand Law</title>
<link href="https://fonts.googleapis.com/css2?family=Lato:wght@300;400;700;900&family=Montserrat:wght@400;500;600&display=swap" rel="stylesheet">
<style>
:root{
  --blue:#4f8fce;
  --ink:#333333;
  --muted:#9a9a9a;
  --band:#ececec;
  --soft:#f5f5f3;
  --footer:#1e1e1e;
  --footer-text:#bdbdbd;
  --white:#ffffff;
  --black:#000000;
}
*{box-sizing:border-box;margin:0;padding:0}
html,body{width:1200px;height:2217px;overflow:hidden}
body{position:relative;background:var(--white);font-family:"Lato",sans-serif;color:var(--ink)}
.abs{position:absolute}

/* header */
.site-header{left:0;top:0;width:1200px;height:67px;background:var(--white);box-shadow:0 1px 3px rgba(0,0,0,.12);z-index:2}
.brand{left:129px;top:12px;font-weight:300;font-size:44px;letter-spacing:1px;color:var(--blue);line-height:44px}
.main-nav{left:672px;top:26px;display:flex;gap:27px;font-family:"Montserrat",sans-serif;font-size:11.5px;letter-spacing:.4px;color:var(--ink);white-space:nowrap}

/* hero */
.hero{left:0;top:67px;width:1200px;height:598px;
  background:linear-gradient(100deg,#c9c7c2 0%,#9a9c9f 8%,#7b7f84 18%,#e8e6e2 24%,#6f7377 32%,#55585c 42%,#8d8882 50%,#3b3a3d 60%,#4a4b52 72%,#a9a49c 84%,#d7d3cc 100%)}
.hero-shade{left:560px;top:67px;width:640px;height:598px;background:linear-gradient(90deg,rgba(0,0,0,0),rgba(0,0,0,.22))}
.hero-title{left:605px;top:208px;width:540px;font-weight:900;font-size:47px;line-height:57px;color:var(--white);text-transform:uppercase}
.hero-rule{left:605px;top:387px;width:459px;height:1px;background:rgba(255,255,255,.7)}
.hero-text{left:605px;top:403px;width:440px;font-size:18.5px;line-height:23px;color:var(--white)}
.btn-consult{left:601px;top:501px;width:234px;height:44px;border-radius:22px;background:var(--blue);color:var(--white);font-weight:700;font-size:18px;display:flex;align-items:center;justify-content:center}
.btn-learn{left:872px;top:509px;font-weight:700;font-size:18px;color:var(--black);border-bottom:3px solid var(--black);padding-bottom:2px}

/* press band */
.press{left:0;top:668px;width:1200px;height:72px;background:var(--band);display:flex;align-items:center}
.press-label{margin-left:87px;width:124px;font-size:20px;color:var(--ink);white-space:nowrap}
.press-item{height:72px;display:flex;align-items:center;justify-content:center;border-left:1px solid #d8d8d8;font-weight:900;font-size:15px;color:var(--ink);white-space:nowrap}

/* practice areas */
.section-title{font-family:"Montserrat",sans-serif;text-align:center;color:var(--ink)}
.practice-title{left:0;top:778px;width:1200px;font-size:33px;font-weight:500}
.practice{width:300px;text-align:center}
.practice-icon{display:block;margin:0 auto}
.practice-name{margin-top:24px;font-size:17px;color:#555}
.practice-desc{margin:15px auto 0;width:264px;font-size:12.5px;line-height:18.5px;color:var(--muted)}

/* understanding */
.understand{left:0;top:1119px;width:1200px;height:418px;background:var(--soft)}
.understand-title{left:0;top:1154px;width:1200px;font-size:38px;font-weight:500;letter-spacing:1px}
.understand-sub{left:0;top:1200px;width:1200px;font-size:19px}
.card{top:1259px;width:340px;height:309px;background:var(--black)}
.card-photo{width:340px;height:230px}
.card-title{padding:14px 6px 0;font-family:"Montserrat",sans-serif;font-size:19px;color:var(--white);line-height:20px}
.card-text{padding:4px 6px 0;font-size:14px;line-height:17px;color:var(--white)}

/* cta band */
.cta{left:0;top:1601px;width:1200px;height:224px;background:var(--blue)}
.cta-title{left:0;top:1650px;width:1200px;text-align:center;font-weight:700;font-size:38px;color:var(--white)}
.cta-sub{left:0;top:1695px;width:1200px;text-align:center;font-size:24px;color:var(--white)}
.btn-cta{left:488px;top:1737px;width:224px;height:49px;border-radius:10px;background:var(--black);color:var(--white);font-weight:700;font-size:18px;display:flex;align-items:center;justify-content:center}

/* footer */
.site-footer{left:0;top:1825px;width:1200px;height:392px;background:var(--footer)}
.footer-brand{left:127px;top:1888px;font-weight:300;font-size:60px;letter-spacing:1px;color:#8a8a8a;line-height:60px}
.social{left:127px;top:2030px;display:flex;gap:28px}
.social span{width:26px;height:26px;border-radius:50%;background:#cfcfcf}
.footer-head{top:1866px;font-family:"Montserrat",sans-serif;font-weight:600;font-size:19px;color:var(--white)}
.quick-links{left:406px;top:1910px;list-style:none;font-size:13px;color:var(--footer-text);line-height:34px}
.news{left:587px;top:1912px;width:240px}
.news-item{display:flex;gap:12px;margin-bottom:22px}
.news-dot{width:14px;height:14px;border-radius:50%;background:var(--blue);flex:none;margin-top:5px}
.news-text{width:192px;font-size:13px;line-height:25px;color:var(--footer-text)}
.news-text a{color:var(--blue);text-decoration:none}
.address{left:876px;top:1914px;list-style:none;width:200px}
.address li{display:flex;gap:12px;font-size:11px;line-height:24px;color:var(--footer-text);margin-bottom:10px}
.address li::before{content:"";width:10px;height:1px;background:var(--footer-text);margin-top:12px;flex:none}
.footer-rule{left:0;top:2150px;width:1200px;height:1px;background:#3a3a3a}
.copyright{left:129px;top:2175px;font-size:13px;color:var(--white)}
.copyright span{color:var(--blue)}
.live-chat{left:751px;top:2176px;width:319px;height:41px;background:var(--black);display:flex;align-items:center;padding:0 12px;font-size:13px;color:var(--white)}
.live-chat .chat-controls{margin-left:auto;display:flex;gap:5px}
.live-chat .chat-controls span{width:20px;height:18px;background:var(--white);border-radius:2px}
</style>
</head>
<body>

<header class="abs site-header">
  <div class="abs brand">MOLAW</div>
  <nav class="abs main-nav">
    <span>HOME</span><span>ABOUT</span><span>PRACTICE AREA</span><span>BLOG</span><span>CONTACT</span>
  </nav>
</header>

<div class="abs hero" role="img" aria-label="Smiling grey-haired attorney in a grey suit and glasses in front of colleagues on a city street"></div>
<div class="abs hero-shade"></div>
<h1 class="abs hero-title">Welcome to Marwick Ostrand Law Firm</h1>
<div class="abs hero-rule"></div>
<p class="abs hero-text">Great success rate, recovering millions every year since 1992. If you or someone you love has suffered the consequences of another person's negligence.</p>
<div class="abs btn-consult">Free Consultation</div>
<div class="abs btn-learn">Learn More</div>

<section class="abs press">
  <div class="press-label">As seen in:</div>
  <div class="press-item" style="width:105px">Metro Wire</div>
  <div class="press-item" style="width:182px">Channel Nine Report</div>
  <div class="press-item" style="width:183px">Evening Dispatch</div>
  <div class="press-item" style="width:133px">Ledger</div>
  <div class="press-item" style="width:185px">The Capitol Courier</div>
  <div class="press-item" style="width:124px">Coast News</div>
</section>

<h2 class="abs section-title practice-title">OUR PRACTICE AREAS</h2>

<div class="abs practice" style="left:112px;top:845px">
  <svg class="practice-icon" width="116" height="116" viewBox="0 0 116 116">
    <circle cx="58" cy="58" r="58" fill="#4f8fce"/>
    <g fill="#fff">
      <circle cx="38" cy="36" r="6"/><rect x="31" y="44" width="14" height="34" rx="3"/>
      <circle cx="60" cy="36" r="6"/><path d="M53 44h14l5 22h-24z"/><rect x="55" y="64" width="10" height="16"/>
      <circle cx="80" cy="50" r="5"/><rect x="74" y="57" width="12" height="22" rx="3"/>
    </g>
  </svg>
  <div class="practice-name">Family Law</div>
  <p class="practice-desc">Alias, porro, consequatur quas nostrum sed iure quos quia excepturi rerum libero odit maxime explicabo ducimus?</p>
</div>

<div class="abs practice" style="left:450px;top:845px">
  <svg class="practice-icon" width="116" height="116" viewBox="0 0 116 116">
    <circle cx="58" cy="58" r="58" fill="#ececec"/>
    <g fill="none" stroke="#4f8fce" stroke-width="2.5">
      <line x1="58" y1="34" x2="58" y2="86"/><line x1="30" y1="44" x2="86" y2="44"/>
      <rect x="50" y="22" width="16" height="14" rx="2"/>
      <path d="M34 44l-9 20h18zM82 44l-9 20h18z"/>
      <line x1="46" y1="86" x2="70" y2="86"/>
    </g>
  </svg>
  <div class="practice-name">Civil litigation</div>
  <p class="practice-desc">Alias, porro, consequatur quas nostrum sed iure quos quia excepturi rerum libero odit maxime explicabo ducimus?</p>
</div>

<div class="abs practice" style="left:784px;top:845px">
  <svg class="practice-icon" width="116" height="116" viewBox="0 0 116 116">
    <circle cx="58" cy="58" r="58" fill="#ececec"/>
    <g fill="none" stroke="#4f8fce" stroke-width="2.5">
      <circle cx="76" cy="44" r="12"/><circle cx="42" cy="76" r="12"/>
      <path d="M66 50l-6 6M56 60l-4 4"/>
    </g>
  </svg>
  <div class="practice-name">Criminal Defense</div>
  <p class="practice-desc">Alias, porro, consequatur quas nostrum sed iure quos quia excepturi rerum libero odit maxime explicabo ducimus?</p>
</div>

<section class="abs understand"></section>
<h2 class="abs section-title understand-title">UNDERSTANDING YOU</h2>
<p class="abs section-title understand-sub">We take the time to understand your circumstances.</p>

<article class="abs card" style="left:84px">
  <div class="card-photo" role="img" aria-label="Hand writing notes in a notebook beside a coffee cup and phone on a white table" style="background:linear-gradient(125deg,#f4f3f1 0%,#e2e1de 25%,#c9c8c6 45%,#8f8d8f 62%,#d9d4cc 75%,#6e6b6e 100%)"></div>
  <div class="card-title">IDENTIFY THE ISSUES</div>
  <div class="card-text">We help you break down your legal problems</div>
</article>
<article class="abs card" style="left:430px">
  <div class="card-photo" role="img" aria-label="Smiling couple reviewing documents together in a bright office" style="background:linear-gradient(100deg,#cfd9e4 0%,#e6d8c8 22%,#b99778 38%,#f3efea 55%,#7a5a44 66%,#eeeae6 80%,#c8c2bc 100%)"></div>
  <div class="card-title">STRUCTURED ADVICE</div>
  <div class="card-text">We give you clear legal advice about your options</div>
</article>
<article class="abs card" style="left:776px">
  <div class="card-photo" role="img" aria-label="Hands typing on a laptop keyboard at a wooden desk" style="background:linear-gradient(160deg,#2e201a 0%,#5b3c2c 25%,#c7c9cf 45%,#8a6450 62%,#d9c9d6 80%,#b8a6b9 100%)"></div>
  <div class="card-title">RESEARCH &amp; ANALYSIS</div>
  <div class="card-text">We examine your case to find the best solution for you</div>
</article>

<section class="abs cta"></section>
<h2 class="abs cta-title">Solving legal Problems Reducing Stress</h2>
<p class="abs cta-sub">The real cost of legal issues can be to your health</p>
<div class="abs btn-cta">Learn More</div>

<footer class="abs site-footer"></footer>
<div class="abs footer-brand">MOLAW</div>
<div class="abs social"><span></span><span></span><span></span><span></span></div>

<h3 class="abs footer-head" style="left:406px">QUICK LINKS</h3>
<ul class="abs quick-links">
  <li>Home</li><li>About Us</li><li>Family law</li><li>Civil litigation</li><li>Conveyancing</li><li>Contact</li>
</ul>

<h3 class="abs footer-head" style="left:587px">LATEST NEWS</h3>
<div class="abs news">
  <div class="news-item"><span class="news-dot"></span><p class="news-text">World travel agecny make deal with us . . .<br><a>http://mo.example/n1</a></p></div>
  <div class="news-item"><span class="news-dot"></span><p class="news-text">World travel agecny make deal with us . . .<br><a>http://mo.example/n1</a></p></div>
</div>

<h3 class="abs footer-head" style="left:876px">OUR ADDRESS</h3>
<ul class="abs address">
  <li>Level 2, Harbor Court 14-18 Alder Street Westvale CA 95814</li>
  <li>(02) 5550 0142</li>
  <li>office@marwickostrand.example</li>
  <li>9:00pm - 5:00pm<br>Sunday Closed</li>
</ul>

<div class="abs footer-rule"></div>
<p class="abs copyright">Copyright <span>Marwick Ostrand Law</span> @2017</p>
<div class="abs live-chat">Live Chat<div class="chat-controls"><span></span><span></span></div></div>

</body>
</html>
```